Photography Prints Business Card Design

Background info: Nature, flower, landscape,  macro, wildlife photographer. Shoot color and B&W images. Sell prints at juried fine art shows.
Looking for two-sided, clean, memorable design with creative use of my initials, DK.   I like the DK symbol in the my logo. Just use the DK symbol. Do not leave the underlying text as uploaded by me. I do not like the serif font and positioning of the words!  Either  remove the small print "Dorian Kessler Photography" under the logo,  or change to a sans serif font, or reposition with "Dorian Kessler" above "Photography" which seems to work with serif fonts.
Target Market(s)
Sophisticated art buyers, post-college to middle age
Industry/Entity Type
Business
Contact Information for Business Card
Dorian Kessler Photography
842 Harrow Bend CT
Alder Springs, OR 97455
(555) 214-0148
www.doriankessler.com
PW:kesslerphoto
dorian@doriankessler.com
If using just one line address, make sure there is a comma after  "CT" in street address. For example:
842 Harrow Bend CT, Alder Springs, OR 97455
Requirements
Must have
- 1.Two-sided card submitted as one design.
2. Must use the DK symbol in my logo.
3. Do not leave the text "Dorian Kessler Photography" under the DK symbol in the logo uploaded by me. I do not like that serif font or the positioning of the words! Either remove the small print "Dorian Kessler Photography" under the logo entirely, or change text to a sans serif font, or reposition text with "Dorian Kessler" above "Photography" which seems to work with serif fonts.
Nice to have
- Can use my DK logo (three file types uploaded: AI, PSD, TIF)  I  like the attached B&W water droplet photo.  My pictures on my website, www.doriankkessler.com  can also be used.  Possible use of Pinwave logo with (either the "f" alone or the square blue icon with white "f") my PW page short url name: kesslerphoto.
Should not have
- 1.No icons or pictures  of camera or lenses or other photographic gear or film strips.
2. No QR or other "barcode" type symbols.
3. No outlining of my logo symbol (drop shadow possibly).
4. No decorative or outlined fonts.
5. I am not a fan of most script fonts.
6. No play on "Kessler" such as snow or other winter season symbols.
7. Do not keep the original text, "Dorian Kessler Photography" under DK logo. Change it or remove it entirely.

```html
<!DOCTYPE html>
<html lang="en">
<head>
<meta charset="utf-8">
<title>Dorian Kessler Photography – Business Card</title>
<link rel="stylesheet" href="https://fonts.googleapis.com/css2?family=Montserrat:wght@400;500;600&family=Great+Vibes&display=swap">
<style>
  :root {
    --page: #d9d6d2;
    --card-black: #050505;
    --band-front: #2a2a2a;
    --band-back: #141414;
    --photo-dark: #0b0b0b;
    --photo-mid: #6e6e6e;
    --photo-light: #c9c9c9;
    --text-light: #ffffff;
    --text-soft: #e4e4e4;
    --divider: #8a8a8a;
  }
  * { box-sizing: border-box; margin: 0; padding: 0; }
  html, body { width: 1200px; height: 1000px; overflow: hidden; }
  body {
    background: var(--page);
    font-family: "Montserrat", Arial, sans-serif;
    color: var(--text-light);
    position: relative;
  }
  .card {
    position: absolute;
    width: 760px;
    height: 434px;
    background: var(--card-black);
    overflow: hidden;
    box-shadow: 0 8px 24px rgba(0,0,0,.35);
  }
  /* Front side */
  .card-front { left: 60px; top: 40px; }
  .front-photo {
    position: absolute; inset: 0 0 64px 0;
    background:
      radial-gradient(ellipse at 85% 25%, rgba(220,220,220,.55) 0 8%, transparent 14%),
      radial-gradient(ellipse at 35% 55%, rgba(220,220,220,.45) 0 6%, transparent 11%),
      linear-gradient(165deg, var(--photo-dark) 0%, var(--photo-dark) 42%, var(--photo-mid) 62%, var(--photo-light) 100%);
  }
  .front-logo {
    position: absolute; left: 60px; top: 70px;
    font-weight: 600; font-size: 64px; letter-spacing: 2px; line-height: 1;
    color: var(--text-light);
  }
  .front-tagline {
    position: absolute; left: 92px; top: 142px;
    font-family: "Great Vibes", cursive; font-size: 26px; color: var(--text-soft);
  }
  .front-band {
    position: absolute; left: 0; right: 0; bottom: 0; height: 64px;
    background: var(--band-front);
  }
  .front-url {
    position: absolute; right: 120px; bottom: 76px;
    font-size: 26px; font-weight: 400; color: var(--text-light);
  }
  /* Back side */
  .card-back { left: 380px; top: 526px; }
  .back-photo {
    position: absolute; left: 0; right: 0; top: 150px; height: 140px;
    background:
      radial-gradient(ellipse at 88% 40%, rgba(150,150,150,.45) 0 12%, transparent 20%),
      radial-gradient(ellipse at 36% 45%, rgba(150,150,150,.35) 0 8%, transparent 14%),
      linear-gradient(180deg, var(--card-black) 0%, #2c2c2c 60%, #3a3a3a 100%);
  }
  .back-logo {
    position: absolute; left: 0; right: 0; top: 60px; text-align: center;
    font-weight: 600; font-size: 78px; letter-spacing: 2px; line-height: 1;
  }
  .back-name {
    position: absolute; left: 0; right: 0; top: 200px; text-align: center;
    font-weight: 400; font-size: 34px; letter-spacing: .5px;
  }
  .back-tagline {
    position: absolute; left: 0; right: 0; top: 242px; text-align: center;
    font-family: "Great Vibes", cursive; font-size: 30px; color: var(--text-soft);
  }
  .back-band {
    position: absolute; left: 0; right: 0; bottom: 0; height: 144px;
    background: var(--band-back);
    display: flex; align-items: center; justify-content: center;
    font-size: 17px; line-height: 1.45; color: var(--text-soft);
  }
  .contact-list { list-style: none; padding-right: 34px; }
  .contact-list li { display: flex; align-items: center; gap: 10px; }
  .contact-list svg { width: 16px; height: 16px; flex: none; }
  .divider { width: 1px; height: 88px; background: var(--divider); }
  .address { padding-left: 34px; font-style: normal; }
</style>
</head>
<body>
  <section class="card card-front" aria-label="Card front">
    <div class="front-photo" role="img" aria-label="Black and white macro photograph of water droplets on a leaf"></div>
    <div class="front-logo">DK</div>
    <div class="front-tagline">Photography</div>
    <div class="front-band"></div>
    <div class="front-url">www.doriankessler.com</div>
  </section>

  <section class="card card-back" aria-label="Card back">
    <div class="back-photo" role="img" aria-label="Dim black and white photograph of water droplets"></div>
    <div class="back-logo">DK</div>
    <div class="back-name">Dorian Kessler</div>
    <div class="back-tagline">Photography</div>
    <div class="back-band">
      <ul class="contact-list">
        <li><svg viewBox="0 0 16 16"><rect x="3" y="3" width="10" height="10" fill="#e4e4e4"/></svg>kesslerphoto</li>
        <li><svg viewBox="0 0 16 16"><path d="M4 1.5l2.5 3-1.5 1.6c.8 1.8 2.2 3.3 4 4.1l1.6-1.5 3 2.4-1.6 2.6C7 13.4 2.6 9 1.4 3.1z" fill="#e4e4e4"/></svg>(555) 214-0148</li>
        <li><svg viewBox="0 0 16 16"><rect x="1" y="3" width="14" height="10" fill="#e4e4e4"/><path d="M1 3l7 6 7-6" fill="none" stroke="#141414" stroke-width="1.4"/></svg>dorian@doriankessler.com</li>
      </ul>
      <div class="divider"></div>
      <address class="address">842 Harrow Bend CT,<br>Alder Springs,<br>OR 97455</address>
    </div>
  </section>
</body>
</html>
```